Need brochure designed for my marijuana web startup.

PLEASE READ THE INSTRUCTIONS THOROUGHLY. YOUR SUBMISSION WILL BE REJECTED IF THEY ARE NOT FOLLOWED.

may lead to other immediate design work, such as flyers, postcards, banners, etc.

I need a PRINT trifold brochure or pamphlet designed for my company, Leafbrook.net. We are a bootstrapped medical marijuana search engine, locator, listing service and community.

I will be selling my web product and services to medical marijuana dispensaries and would like to quickly demonstrate why my service is better over my competitors..

I have drafted a (poorly designed) brochure that talks about all the points I wanted to hit on. I'd also like to add our 3 pricing plans in the brochure, but if there isn't any room, i'm fine with that.

I received some design guidelines from a branding consulting firm, so the designs must adhere to those rules. These guidelines are attached as a pdf. These guidelines include things like minimum clear space for the logo, primary and secondary colors, and font style.

Target Market(s)

marijuana dispensaries

Industry/Entity Type

Startup

Font styles to use
Other font styles liked:
• gotham rounded

Colors
9bcb3b

Requirements
Must have
• follow the design guidelines attached, including colors used! font files are attached.
• this is a PRINT brochure request. can be trifold, or 1 fold.
• The TEXT or "COPY" is all included in the brochure.doc attachment. There is additional stats in the "Nice to Haves" section that you may or may not include. up to you. Pricing info is included as an attachment called "Pricing Plan"
• please, keep it simple!
Nice to have
• some graphics.
• pricing plan.
• some statistics that may be interesting to help highlight how special unique items that are hard to find can be easily found with my service:
• From a sample of 2,594 active listings, there are over 153,000 items being sold:
• 12,900 marijuana related accessories (bongs, pipes, clothes, vapor pens, etc.)
• 20,300 concentrates
• 40,400 edibles
• 52,400 flowers (bud and shakes)
• 21,500 other - oral (pills, sprays), topical (lotions, soaps), seeds, oils
• 5,500 pre-rolled marijuana cigarettes (joints, blunts)
• of the 153,000 items, there are:
• 17,750+ hybrid items
• 27,100+ indica items
• 15,000+ sativa items
• in the world of edibles, there are:
• 200+ gluten free items
• 300+ sugar free items
• doses in edibles range from .3mg to 2,353mg (i.e. olive oil) the recommended dosage is 5-10mg
• 2,900+ items of 100mg edibles make it the most common dose offered on the market.
• there are over 4,000 items that are high in CBD (the medicinal chemical of weed).
Should not have
• no photos.

```html
<!DOCTYPE html>
<html lang="en">
<head>
<meta charset="utf-8">
<title>Leafbrook.net – Trifold Brochure Inside Spread</title>
<link rel="stylesheet" href="https://fonts.googleapis.com/css2?family=Questrial&family=Varela+Round&family=Open+Sans:ital,wght@0,400;0,700;1,400&family=Montserrat:ital,wght@1,700&display=swap">
<style>
  :root {
    --green: #3f9b35;
    --lime: #8dc63f;
    --teal: #305f6c;
    --tab: #4b5048;
    --navy: #2d5a74;
    --ink: #1c1c1c;
    --icon: #4e5355;
    --yellow: #d9d24b;
    --white: #ffffff;
    --frame: #d6d6d6;
  }
  * { margin: 0; padding: 0; box-sizing: border-box; }
  html, body { width: 1200px; height: 1000px; overflow: hidden; background: var(--white); }
  .spread { position: relative; width: 1200px; height: 1000px; font-family: "Open Sans", Arial, sans-serif; color: var(--ink); }
  .sheet { position: absolute; left: 33px; top: 62px; width: 1136px; height: 879px; border: 1px solid var(--frame); }
  .flow-lines { position: absolute; left: 0; top: 0; }
  .abs { position: absolute; }

  /* Why leafbrook */
  .why-word { left: 70px; top: 70px; font: 100px/1 "Questrial", sans-serif; color: var(--green); letter-spacing: -2px; }
  .why-brand { left: 70px; top: 170px; font: 46px/1 "Questrial", sans-serif; color: var(--green); letter-spacing: -1px; }
  .why-mark { left: 308px; top: 95px; font: 160px/1 "Questrial", sans-serif; color: var(--green); }
  .stat { right: 828px; font: 15px/1 "Varela Round", sans-serif; color: var(--ink); display: flex; align-items: center; gap: 6px; }
  .stat i { width: 17px; height: 17px; border-radius: 50%; background: var(--icon); color: var(--white); font: 700 12px/17px "Open Sans", sans-serif; font-style: normal; text-align: center; }
  .stat-note { right: 828px; top: 289px; font: 10px/1 "Varela Round", sans-serif; font-variant: small-caps; letter-spacing: .3px; }

  /* Big data */
  .amp { left: 60px; top: 398px; font: 96px/1 "Questrial", sans-serif; color: var(--green); }
  .bigdata { font: 44px/1 "Questrial", sans-serif; color: var(--green); letter-spacing: -1px; }
  .bigdata-lead { left: 80px; top: 535px; width: 295px; font: 700 13.5px/20px "Open Sans", sans-serif; }
  .body-copy { font: 13.5px/20px "Open Sans", sans-serif; }

  /* Compassionate care */
  .cc-title { left: 436px; top: 112px; font: 45px/1 "Questrial", sans-serif; color: var(--green); letter-spacing: -.5px; }
  .cc-care { left: 548px; top: 162px; font: 80px/1 "Questrial", sans-serif; color: var(--green); }
  .cc-plus { left: 457px; top: 168px; }
  .cc-quote { left: 425px; top: 263px; width: 355px; text-align: center; font: italic 19px/25px "Open Sans", sans-serif; }
  .cc-copy { left: 423px; top: 440px; width: 355px; font: 13.5px/25px "Open Sans", sans-serif; }
  .site-screen { left: 432px; top: 562px; width: 208px; height: 175px; border-radius: 6px; background: linear-gradient(180deg, #e9ecea 0%, #e9ecea 22%, #5a5750 23%, #3a3832 100%); border: 6px solid #1e1f20; }
  .site-stand { left: 505px; top: 737px; width: 62px; height: 38px; background: linear-gradient(180deg, #c9cbcd, #f0f1f2); border-radius: 0 0 6px 6px; }

  /* Benefits panel */
  .panel-tab { left: 870px; top: 120px; width: 288px; height: 40px; background: var(--tab); border-radius: 26px 26px 0 0; }
  .panel { left: 858px; top: 143px; width: 311px; height: 797px; background: var(--teal); }
  .benefits-title { left: 905px; top: 165px; color: var(--yellow); font: 36px/1 "Questrial", sans-serif; letter-spacing: -1px; }
  .benefits-title b { font: 700 50px/1 "Varela Round", sans-serif; letter-spacing: 0; }
  .benefits-brand { left: 925px; top: 202px; color: var(--yellow); font: 38px/1 "Questrial", sans-serif; letter-spacing: -1px; }
  .benefit-icon { left: 792px; width: 94px; height: 94px; border-radius: 50%; background: var(--lime); }
  .benefit-icon svg { display: block; }
  .benefit-text { left: 946px; width: 210px; color: var(--white); font: 17px/21px "Varela Round", sans-serif; }
  .soon { left: 888px; top: 715px; color: var(--yellow); font: italic 700 34px/1 "Montserrat", sans-serif; letter-spacing: -.5px; }
  .soon-item { right: 57px; color: var(--yellow); font: 14px/1 "Varela Round", sans-serif; letter-spacing: 1.2px; text-align: right; }
</style>
</head>
<body>
<div class="spread">
  <div class="sheet"></div>

  <svg class="flow-lines" width="1200" height="1000" viewBox="0 0 1200 1000" aria-hidden="true">
    <polygon points="34,262 34,292 312,578 432,578 432,570 320,570" fill="var(--navy)"/>
    <polygon points="640,698 680,698 858,888 854,888 676,704 640,704" fill="var(--navy)"/>
  </svg>

  <!-- Why leafbrook -->
  <div class="abs why-word">why</div>
  <div class="abs why-brand">leafbrook</div>
  <div class="abs why-mark">?</div>
  <div class="abs stat" style="top:242px"><i>!</i>Hard to find items can be easily found</div>
  <div class="abs stat" style="top:270px"><i>!</i>12,900 marijuana accessories</div>
  <div class="abs stat-note">bongs, pipes, clothes, vapor pens and more!</div>
  <div class="abs stat" style="top:309px"><i>!</i>Access over 153,000 items</div>
  <div class="abs stat" style="top:339px"><i>!</i>17,750+ hybrid items</div>
  <div class="abs stat" style="top:363px"><i>!</i>27,100+ indica items</div>
  <div class="abs stat" style="top:387px"><i>!</i>15,000+ sativa items</div>

  <!-- Big data -->
  <div class="abs amp">&amp;</div>
  <div class="abs bigdata" style="left:118px;top:417px">big</div>
  <div class="abs bigdata" style="left:128px;top:456px">data</div>
  <div class="abs bigdata" style="left:94px;top:494px">marijuana</div>
  <p class="abs bigdata-lead">With the ever increasing number of strains, marijuana products and dispensaries flooding the market, it has become increasingly difficult for consumers to find that “one” item.</p>
  <p class="abs body-copy" style="left:80px;top:653px;width:300px">The menus offered by most listing services are very limited in the amount of metadata they provide, so searching for a particular strain or item is almost impossible.</p>
  <p class="abs body-copy" style="left:80px;top:735px;width:300px">By properly labeling and tagging all the different strains and products with these additional metadata attributes, we have created a powerful search engine to help consumers find very specific items, like Blue Dream Shatter, Grape Ape c02 oil, and even medicated pizzas in their local neighborhood.</p>

  <!-- Compassionate care -->
  <div class="abs cc-title">compassionate</div>
  <svg class="abs cc-plus" width="90" height="95" viewBox="0 0 90 95" aria-hidden="true">
    <path d="M30 6 Q30 0 36 0 H54 Q60 0 60 6 V33 H84 Q90 33 90 39 V56 Q90 62 84 62 H60 V89 Q60 95 54 95 H36 Q30 95 30 89 V62 H6 Q0 62 0 56 V39 Q0 33 6 33 H30 Z" fill="var(--icon)"/>
  </svg>
  <div class="abs cc-care">CARE</div>
  <p class="abs cc-quote">Where would this industry be today if it weren’t for the early pioneers of Compassionate Care? Unfortunately for most services, “compassion” has lost to greed, but we’re here to bring it back!</p>
  <p class="abs cc-copy">We take care of all our leafbrook dispensaries by offering very reasonable prices with no hidden costs and easy to understand plans that have features well beyond our competitors. All of our plans offer a free month trial so you can try before you buy.</p>
  <div class="abs site-screen" role="img" aria-label="Desktop monitor showing the Leafbrook.net website home page"></div>
  <div class="abs site-stand" aria-hidden="true"></div>
  <p class="abs cc-copy" style="top:782px">We also don’t accept bribes for favorable search rankings, bigger map markers, or any other unfair features our competitors offer. We believe every dispensary should have a fair chance of success.</p>

  <!-- Benefits panel -->
  <div class="abs panel-tab"></div>
  <div class="abs panel"></div>
  <div class="abs benefits-title">benefits<b>OF</b></div>
  <div class="abs benefits-brand">leafbrook</div>

  <div class="abs benefit-icon" style="top:271px">
    <svg width="94" height="94" viewBox="0 0 94 94" aria-hidden="true">
      <path d="M14 40 C14 24 28 16 42 16 C58 16 70 25 70 40 C70 54 57 62 42 62 L36 62 L24 72 L26 60 C18 56 14 49 14 40 Z" fill="var(--icon)" stroke="var(--lime)" stroke-width="3"/>
      <path d="M50 60 C50 50 58 45 66 45 C75 45 82 51 82 59 C82 65 79 69 74 71 L76 80 L67 73 L66 73 C57 73 50 68 50 60 Z" fill="var(--icon)" stroke="var(--lime)" stroke-width="3"/>
    </svg>
  </div>
  <p class="abs benefit-text" style="top:282px">Users can follow your dispensary and items to get instant alerts when you update things like price and specials.</p>

  <div class="abs benefit-icon" style="top:416px">
    <svg width="94" height="94" viewBox="0 0 94 94" aria-hidden="true">
      <circle cx="52" cy="36" r="17" fill="none" stroke="var(--icon)" stroke-width="7"/>
      <line x1="41" y1="50" x2="28" y2="77" stroke="var(--icon)" stroke-width="10" stroke-linecap="round"/>
    </svg>
  </div>
  <p class="abs benefit-text" style="top:430px">Our map focuses on one listing at a time, so your map marker always stands out and is never obscured by other markers.</p>

  <div class="abs benefit-icon" style="top:596px">
    <svg width="94" height="94" viewBox="0 0 94 94" aria-hidden="true">
      <g fill="var(--icon)">
        <rect x="38" y="14" width="20" height="66" rx="9" transform="rotate(45 48 47)"/>
        <rect x="38" y="14" width="20" height="66" rx="9" transform="rotate(-45 48 47)"/>
      </g>
    </svg>
  </div>
  <p class="abs benefit-text" style="top:618px">We do not manipulate search rankings for the highest bidder.</p>

  <div class="abs soon">coming soon...</div>
  <div class="abs soon-item" style="top:767px">ONLINE DISPENSARY</div>
  <div class="abs soon-item" style="top:791px">REGISTRATION</div>
  <div class="abs soon-item" style="top:822px">PATIENT VERIFICATIONS</div>
  <div class="abs soon-item" style="top:853px">ONLINE ORDERING</div>
</div>
</body>
</html>
```